KVT Business Cards

We require business cards for our business. We would like a matte black back to the card, with our logo centred in the middle. The front side of the card is open to design.

Target Market(s)

Clients looking for legal services (professional)

Industry/Entity Type

Legal

Contact Information for Business Card

Boris Telemark
Partner
Mobile: 0438 715 642
Email: boris@kvtlaw.co
Website: www.kvtlaw.co
Level 3, 118 Wexbury Street
Sydney NSW 2000

Font styles to use
Other font styles liked:
• Avenir

Colors
f04a50
ffffff
1b1b1b

Requirements
Must have
• Black back with logo included in the centre of the card.
• Our font is Avenir.

```html
<!DOCTYPE html>
<html lang="en">
<head>
<meta charset="utf-8">
<title>KVT Legal – Business Cards</title>
<link rel="stylesheet" href="https://fonts.googleapis.com/css2?family=Nunito+Sans:wght@300;400;600;700&display=swap">
<style>
  :root {
    --ink: #1b1b1b;
    --card: #222222;
    --stage: #2c2c2c;
    --accent: #f04a50;
    --paper: #ffffff;
    --muted: #cfcfcf;
    --silver: #a9a9a9;
  }
  * { box-sizing: border-box; margin: 0; padding: 0; }
  html, body { width: 1200px; height: 895px; overflow: hidden; }
  body {
    background: var(--stage);
    font-family: "Nunito Sans", "Avenir", sans-serif;
    display: flex;
    align-items: center;
    justify-content: center;
    gap: 40px;
  }
  .card {
    width: 540px;
    height: 330px;
    background: var(--card);
    border-radius: 18px;
    border-bottom: 5px solid var(--accent);
    position: relative;
    overflow: hidden;
  }

  /* Back: firm name centred */
  .card-back { display: flex; align-items: center; justify-content: center; }
  .brand { display: flex; align-items: center; gap: 18px; }
  .brand-mark { width: 46px; height: 46px; background: var(--silver); }
  .brand-name {
    color: var(--silver);
    font-weight: 600;
    font-size: 25px;
    line-height: 1.02;
    letter-spacing: 0.5px;
    text-transform: uppercase;
  }

  /* Front: contact details */
  .card-front { padding: 0 40px; }
  .identity {
    position: absolute;
    left: 40px;
    top: 132px;
    text-align: right;
  }
  .person-name {
    color: var(--paper);
    font-weight: 600;
    font-size: 31px;
    letter-spacing: 2.5px;
    text-transform: uppercase;
    line-height: 1;
  }
  .person-role {
    color: var(--accent);
    font-weight: 300;
    font-size: 15px;
    margin-top: 4px;
  }
  .divider {
    position: absolute;
    left: 340px;
    top: 118px;
    width: 1px;
    height: 68px;
    background: var(--muted);
  }
  .contacts {
    position: absolute;
    left: 356px;
    top: 118px;
    list-style: none;
  }
  .contacts li {
    display: flex;
    align-items: center;
    gap: 8px;
    color: var(--muted);
    font-weight: 300;
    font-size: 13.5px;
    height: 22px;
  }
  .contacts svg { width: 13px; height: 13px; flex: none; }
  .contacts .hl { color: var(--accent); }
  .address {
    position: absolute;
    right: 40px;
    bottom: 34px;
    color: var(--muted);
    font-weight: 300;
    font-size: 13.5px;
    letter-spacing: 0.3px;
  }
</style>
</head>
<body>
  <section class="card card-back" aria-label="Card back">
    <div class="brand">
      <span class="brand-mark"></span>
      <p class="brand-name">Kovac Vale<br>Telemark<br>Legal</p>
    </div>
  </section>

  <section class="card card-front" aria-label="Card front">
    <div class="identity">
      <h1 class="person-name">Boris Telemark</h1>
      <p class="person-role">Partner</p>
    </div>
    <span class="divider"></span>
    <ul class="contacts">
      <li>
        <svg viewBox="0 0 14 14" fill="none" stroke="#f04a50" stroke-width="1.4"><rect x="3.5" y="1" width="7" height="12" rx="1.2"/><line x1="6" y1="11" x2="8" y2="11"/></svg>
        0438 715 642
      </li>
      <li>
        <svg viewBox="0 0 14 14" fill="none" stroke="#f04a50" stroke-width="1.4"><rect x="1" y="3" width="12" height="8.5" rx="1"/><polyline points="1.5,3.5 7,8 12.5,3.5"/></svg>
        <span>boris@<span class="hl">kvtlaw</span>.co</span>
      </li>
      <li>
        <svg viewBox="0 0 14 14" fill="none" stroke="#f04a50" stroke-width="1.4"><circle cx="7" cy="6" r="4.5"/><line x1="4" y1="9.5" x2="2" y2="12.5"/></svg>
        <span>www.<span class="hl">kvtlaw</span>.co</span>
      </li>
    </ul>
    <p class="address">Level 3, 118 Wexbury Street, Sydney NSW 2000</p>
  </section>
</body>
</html>
```